Wine label design for my wife. Wine called "The Marisse"

I need a wine label face lift of one of my premium wines in my collection. My wine sells in Harbor Pell's all over the States. My current label is called The Marisse (my wife's name) and the illustration of her eyes is done by a well know artist from South Africa. I do not have to use this illustration and therefor I attached several pictures of her and her eyes, even when she was a little girl. The wine's also made in South Africa. This is a premium wine that we only sell 2000 bottles per year. The wine sells at 60 usd per bottle, The current label is too white. I also think her eyes should look more at the person buying it, than away from them.

Target Market(s)

Top end wine buyers

Font styles to use
Decorative
Script

Requirements
Must have
• 'The Marisse' must be on the label
An illustration must be on the label
Basically all the info that's on the current label must be on by law. As per Sample
Nice to have
• Maybe some ideas of her whole face?
Should not have
• any gold colour

```html
<!DOCTYPE html>
<html lang="en">
<head>
<meta charset="utf-8">
<title>The Marisse – Label Colourways</title>
<link rel="stylesheet" href="https://fonts.googleapis.com/css2?family=Cinzel:wght@400;500&family=Pinyon+Script&display=swap">
<style>
  :root {
    --backdrop: #e3e0db;
    --wine-red: #7b3c3b;
    --wine-red-bright: #a63a3e;
    --navy: #22324a;
    --onyx: #1d1d1d;
    --slate-bar: #2c3944;
    --charcoal-bar: #252525;
    --pale-grey: #cfcfcf;
    --ivory: #f4f1ec;
    --photo-light: #d8d8d8;
    --photo-dark: #6e6e6e;
  }
  * { margin: 0; padding: 0; box-sizing: border-box; }
  html, body {
    width: 959px; height: 1200px; overflow: hidden;
    background: var(--backdrop);
  }
  .label-range { position: relative; width: 959px; height: 1200px; }

  .label {
    position: absolute; top: 407px; width: 290px; height: 386px;
    background: var(--panel); overflow: hidden;
  }
  .label--red   { left: 24px;  --panel: var(--wine-red); --title: var(--ivory); --mark: var(--ivory); --bar: var(--slate-bar); --tab: var(--pale-grey); --tab-ink: #333; }
  .label--navy  { left: 334px; --panel: var(--navy); --title: var(--wine-red-bright); --mark: var(--wine-red-bright); --bar: var(--charcoal-bar); --tab: var(--wine-red); --tab-ink: #1d1d1d; }
  .label--onyx  { left: 644px; --panel: var(--onyx); --title: var(--wine-red-bright); --mark: var(--wine-red-bright); --bar: var(--wine-red); --tab: var(--pale-grey); --tab-ink: #333; }

  .portrait-band {
    position: absolute; top: 0; left: 0; width: 100%; height: 89px;
    background: linear-gradient(180deg, var(--photo-dark) 0%, var(--photo-light) 45%, #bdbdbd 100%);
  }

  .monogram {
    position: absolute; top: 109px; left: 50%; transform: translateX(-50%);
    width: 56px; height: 56px; border: 2px solid var(--mark); border-radius: 50%;
    display: flex; align-items: center; justify-content: center;
    font-family: 'Cinzel', serif; font-size: 24px; color: var(--ivory);
  }

  .rule-line {
    position: absolute; left: 33px; width: 224px; height: 1px;
    background: rgba(244, 241, 236, 0.75);
  }
  .rule-line--top { top: 195px; }
  .rule-line--bottom { top: 264px; }

  .title-kicker {
    position: absolute; top: 180px; left: 50%; transform: translateX(-50%);
    padding: 0 10px; background: var(--panel);
    font-family: 'Pinyon Script', cursive; font-size: 25px; line-height: 28px;
    color: var(--title);
  }
  .title-name {
    position: absolute; top: 204px; left: 0; width: 100%; text-align: center;
    font-family: 'Cinzel', serif; font-weight: 400; font-size: 40px; line-height: 48px;
    letter-spacing: 3px; color: var(--title);
  }
  .varietal {
    position: absolute; top: 283px; left: 0; width: 100%; text-align: center;
    font-family: 'Pinyon Script', cursive; font-size: 22px; line-height: 28px;
    color: var(--ivory);
  }

  .maker-bar {
    position: absolute; top: 334px; left: 0; width: 100%; height: 36px;
    display: flex;
  }
  .maker-tab {
    width: 57px; height: 100%; background: var(--tab);
    display: flex; align-items: center; justify-content: center;
    font-family: 'Cinzel', serif; font-size: 10px; color: var(--tab-ink);
  }
  .maker-name {
    flex: 1; background: var(--bar);
    display: flex; align-items: center; justify-content: center;
    font-family: 'Cinzel', serif; font-size: 14px; letter-spacing: 3.2px;
    color: var(--ivory);
  }
</style>
</head>
<body>
<main class="label-range">

  <section class="label label--red">
    <div class="portrait-band" role="img" aria-label="Black and white photograph of Marisse's eyes"></div>
    <div class="monogram">M</div>
    <div class="rule-line rule-line--top"></div>
    <div class="title-kicker">The</div>
    <h1 class="title-name">MARISSE</h1>
    <div class="rule-line rule-line--bottom"></div>
    <p class="varietal">Sauvignon Blanc 2017</p>
    <div class="maker-bar">
      <div class="maker-tab">Frane</div>
      <div class="maker-name">DANIEL FRANE WINE</div>
    </div>
  </section>

  <section class="label label--navy">
    <div class="portrait-band" role="img" aria-label="Black and white photograph of Marisse's eyes"></div>
    <div class="monogram">M</div>
    <div class="rule-line rule-line--top"></div>
    <div class="title-kicker">The</div>
    <h1 class="title-name">MARISSE</h1>
    <div class="rule-line rule-line--bottom"></div>
    <p class="varietal">Sauvignon Blanc 2017</p>
    <div class="maker-bar">
      <div class="maker-tab">Frane</div>
      <div class="maker-name">DANIEL FRANE WINE</div>
    </div>
  </section>

  <section class="label label--onyx">
    <div class="portrait-band" role="img" aria-label="Black and white photograph of Marisse's eyes"></div>
    <div class="monogram">M</div>
    <div class="rule-line rule-line--top"></div>
    <div class="title-kicker">The</div>
    <h1 class="title-name">MARISSE</h1>
    <div class="rule-line rule-line--bottom"></div>
    <p class="varietal">Sauvignon Blanc 2017</p>
    <div class="maker-bar">
      <div class="maker-tab">Frane</div>
      <div class="maker-name">DANIEL FRANE WINE</div>
    </div>
  </section>

</main>
</body>
</html>
```